PREMIUM AGENCY High End Business Card - A+++ Designers Wanted

** DO NOT ATTEMPT TO CONTACT ME THROUGH SEARCHING ON ZINTREL OR EMAILING ME THROUGH MY WEBSITE **

I need a fresh, contemporary business card designed using the logo attached (BRONSALK)

I have attached the font for BRONSALK

It must have a premium look and feel. The business card size must be STANDARD size.

You can submit either/both VERTICAL or HORIZONTAL designs.

FRONT: It must have the following sample information on

Paul Ardley
Director Operations
Mobile +61 452 118 906
Email paulardley@bronsalk.com
www.bronsalk.com

The REAR of the business card must have the words

CREATE INSPIRE TOMORROW

as part of the design, in the same font (NEXA) attached.

The words do not need to be in capitals, or on the same line, please design this as you see it best working.

ADDITIONAL INFORMATION
======================

The BRONSALK logo must be on the front of the card

I want Ultraviolet printing on the final design, to enhance either the NAME of the person OR the BRONSALK logo OR the words on the back of the card.

Target Market(s)

Agency, Advertising Agency, Creative, Designers

Industry/Entity Type

Media

Contact Information for Business Card

Design Agency, Contemporary, Premium look and feel, High Quality

Font styles to use
Serif
Sans Serif
Other font styles liked:
• ATTACHED TO PROJECT

Requirements
Must have
• BLACK & WHITE as the primary design, and if you feel there can be a highlighted colour, then this can be used.
• The Logo ICON attached is blue, this colour must not be changed.
• I have attached the partner brand BRONSALK MEDIA incase you need to manipulate the original files.
• ** DO NOT ATTEMPT TO CONTACT ME THROUGH SEARCHING ON ZINTREL OR EMAILING ME THROUGH MY WEBSITE **
Nice to have
• Must be Premium. I have attached some sample designs, that I like that would be a good inspiration for where this can be taken.
• My favourite design is is the KESTRAVUE2-BUSINESSCARD-TEMPLATE
Should not have
• No funny or silly standard / off the shelf designs

```html
<!DOCTYPE html>
<html lang="en">
<head>
<meta charset="utf-8">
<title>Bronsalk Business Card</title>
<link rel="stylesheet" href="https://fonts.googleapis.com/css2?family=Montserrat:wght@200;300;400;700;800&display=swap">
<style>
  :root {
    --bg: #ececec;
    --sky: #62a8de;
    --ink: #1c1c1c;
    --paper: #ffffff;
  }
  html, body {
    margin: 0;
    padding: 0;
    width: 1200px;
    height: 841px;
    overflow: hidden;
    background: var(--bg);
    font-family: "Montserrat", sans-serif;
  }
  .sheet {
    width: 1200px;
    height: 841px;
    display: flex;
    flex-direction: column;
    align-items: center;
    justify-content: center;
    gap: 40px;
  }
  .card {
    display: block;
    width: 640px;
    height: 366px;
    box-shadow: 0 10px 28px rgba(0,0,0,0.18);
  }
  .fill-sky { fill: var(--sky); }
  .fill-ink { fill: var(--ink); }
  .fill-paper { fill: var(--paper); }
  .brand-name { font-weight: 800; font-size: 52px; letter-spacing: 8px; fill: var(--paper); }
  .tagline { font-weight: 400; font-size: 15px; letter-spacing: 1.5px; fill: var(--ink); }
  .person-first { font-weight: 200; font-size: 54px; letter-spacing: 3px; fill: var(--paper); }
  .person-last { font-weight: 800; font-size: 54px; letter-spacing: 3px; fill: var(--paper); }
  .role-strong { font-weight: 800; font-size: 18px; fill: var(--ink); }
  .role-light { font-weight: 400; font-size: 18px; fill: var(--ink); }
  .contact { font-weight: 300; font-size: 15px; letter-spacing: 0.8px; fill: var(--paper); }
  .web { font-weight: 300; font-size: 15px; letter-spacing: 0.8px; fill: var(--paper); }
  .icon-line { fill: none; stroke: var(--ink); stroke-width: 2; }
</style>
</head>
<body>
<main class="sheet">

  <svg class="card card-rear" viewBox="0 0 700 400" aria-label="Card rear with brand name and tagline">
    <rect class="fill-sky" width="700" height="400"/>
    <polygon class="fill-ink" points="0,0 150,0 70,400 0,400"/>
    <polygon class="fill-ink" points="520,0 700,0 700,400 640,400"/>
    <circle class="fill-ink" cx="150" cy="190" r="16"/>
    <text class="brand-name" x="185" y="208">BRONSALK</text>
    <text class="tagline" x="188" y="246">CREATE INSPIRE TOMORROW</text>
  </svg>

  <svg class="card card-front" viewBox="0 0 700 400" aria-label="Card front with name and contact details">
    <rect class="fill-sky" width="700" height="400"/>
    <polygon class="fill-ink" points="0,0 230,0 0,55"/>
    <polygon class="fill-ink" points="130,400 700,400 700,235"/>

    <text x="200" y="110"><tspan class="person-first">PAUL </tspan><tspan class="person-last">ARDLEY</tspan></text>
    <text x="204" y="140"><tspan class="role-strong">DIRECTOR </tspan><tspan class="role-light">OPERATIONS</tspan></text>

    <g class="icon-phone" transform="translate(172,162)">
      <rect class="icon-line" x="0" y="0" width="13" height="22" rx="2"/>
      <line class="icon-line" x1="4" y1="18" x2="9" y2="18"/>
    </g>
    <text class="contact" x="200" y="180">+61 452 118 906</text>

    <g class="icon-globe" transform="translate(178,204)">
      <circle class="icon-line" cx="0" cy="0" r="11"/>
      <ellipse class="icon-line" cx="0" cy="0" rx="5" ry="11"/>
      <line class="icon-line" x1="-11" y1="0" x2="11" y2="0"/>
    </g>
    <text class="contact" x="200" y="210">paulardley@bronsalk.com</text>

    <text class="web" x="470" y="368">www.bronsalk.com</text>
    <circle class="fill-sky" cx="648" cy="363" r="10"/>
  </svg>

</main>
</body>
</html>
```